Business Identity Stationary

Already have the logo which is in the attached files so only need the Business STationary
1) Double Sided Business Card
2) Letterhead
3) Presentation folder with business card holder on inside cover
4) WIth compliments slip
See information for business cards, letterhead and presentation folder below.
http://files.pixelbazaar-example.com/img/771204/40612/40612_3918825_771204_thumb.jpg
Updates

This should be a simply job using a logo we already had designed along with a little device. I suggest using the device off center and perhaps lower in the corner in an abstract way. Also the logo device could be used as a watermark for the letterhead. The designer who created the logo presented something that I think works well for a business card. The front of the double sided business card could have the name logo small for the website address and only use the Lime device on the front. Then on the back could be the name Brevar Consulting logo.

Please note that for the business card the black and lime green background do look good. Also please think of using the lime device separately in an unusual way.

It has been brought to my attention that.my budget was far to low. Hopefully this.will attract you to the project. 

The parent company of Brevar Consulting is TallHeron investments. I have uploaded a file of the Tall Heron business card I really like. Perhaps use this business card as a guide to the type of modern and clean style I am looking for. It also works to have the Brevar Consultign and Tall Heron similar.

Reason: Still haven't received anything exactly right.

Industry/Entity Type

Business

Font styles to use
Sans Serif

Colors
9bcb3c
000000
5c5c5c
add136
cadf82
eaf2cf
f9fbf2
1b1b1b
757575

Requirements
Must have
• 1) Double Sided Business Card
Marta Delvorin
Director
Tel: +505 8290 3357
Email: mkd@brevarconsulting-example.com
Website: www.brevarconsulting-example.com

Everett Delvorin
Director
Tel: +505 8290 3362
Email: ekd@brevarconsulting-example.com

Lucia Pardo Ventrosa
Director
Tel: 8442 6183
Email: lpv@brevarconsulting-example.com

2) Letterhead
Logo
Lime Logo Device
Website Address: www.brevarconsulting-example.com
Small print on bottom: Brevar Consulting a Tall Heron Investment Company SA. RUC K0720000483915

3) Presentation Folder
Traditional Presentation folder with inside front cover spot for the insertion of business card.

4) With Compliments slip

```html
<!DOCTYPE html>
<html lang="en">
<head>
<meta charset="utf-8">
<title>Brevar Consulting — Business Card</title>
<link rel="stylesheet" href="https://fonts.googleapis.com/css2?family=Questrial&display=swap">
<style>
  :root {
    --lime: #9bcb3c;
    --black: #000000;
    --ink: #1b1b1b;
    --grey: #5c5c5c;
    --grey-light: #757575;
    --grey-soft: #9a9a9a;
    --paper: #ffffff;
    --backdrop: #ececec;
  }
  * { box-sizing: border-box; margin: 0; padding: 0; }
  html, body {
    width: 1200px; height: 1000px; overflow: hidden;
    background: var(--backdrop);
    font-family: "Questrial", "Century Gothic", sans-serif;
  }
  .canvas { position: relative; width: 1200px; height: 1000px; }

  .card {
    position: absolute;
    width: 724px; height: 362px;
    border-radius: 30px;
    overflow: hidden;
    background: var(--paper);
  }

  /* Card back: black bands with white centre stripe */
  .card-back { left: 238px; top: 90px; background: var(--black); }
  .card-back .band {
    position: absolute; left: 0; right: 0;
    top: 104px; height: 150px;
    background: var(--paper);
    display: flex; align-items: center; justify-content: center; gap: 16px;
  }
  .wordmark {
    color: var(--ink);
    font-weight: 400;
    white-space: nowrap;
  }
  .card-back .wordmark { font-size: 50px; letter-spacing: 1px; }
  .brand-dot {
    display: inline-block; border-radius: 50%;
    background: var(--lime);
  }
  .card-back .brand-dot { width: 34px; height: 34px; }

  /* Card front: contact details */
  .card-front { left: 238px; top: 548px; }
  .card-front .brand {
    position: absolute; left: 56px; top: 42px;
    display: flex; align-items: center; gap: 10px;
  }
  .card-front .wordmark { font-size: 24px; letter-spacing: 0.5px; }
  .card-front .brand-dot { width: 16px; height: 16px; }

  .person { position: absolute; left: 58px; top: 146px; }
  .person-name { font-size: 27px; letter-spacing: 1.6px; color: var(--grey); }
  .person-title { font-size: 15px; letter-spacing: 0.8px; color: var(--grey-soft); margin-top: 2px; }

  .contacts { position: absolute; left: 352px; top: 156px; list-style: none; }
  .contacts li {
    display: flex; align-items: center; gap: 5px;
    font-size: 18px; letter-spacing: 0.9px; color: var(--grey);
    height: 29px;
  }
  .contacts .email { font-size: 16.5px; letter-spacing: 0.6px; }
  .contacts svg { flex: none; }

  .company {
    position: absolute; left: 0; right: 0; top: 256px;
    text-align: center; color: var(--grey-light);
    font-size: 15.5px; letter-spacing: 1.6px; line-height: 22px;
  }
  .website {
    position: absolute; left: 0; right: 0; top: 309px;
    text-align: center; color: var(--grey);
    font-size: 19px; letter-spacing: 1.4px; font-weight: 700;
  }
</style>
</head>
<body>
<main class="canvas">

  <section class="card card-back" aria-label="Business card, back">
    <div class="band">
      <span class="wordmark">Brevar Consulting</span>
      <span class="brand-dot" aria-hidden="true"></span>
    </div>
  </section>

  <section class="card card-front" aria-label="Business card, front">
    <div class="brand">
      <span class="wordmark">Brevar Consulting</span>
      <span class="brand-dot" aria-hidden="true"></span>
    </div>

    <div class="person">
      <p class="person-name">Marta Delvorin</p>
      <p class="person-title">Director</p>
    </div>

    <ul class="contacts">
      <li>
        <svg width="14" height="20" viewBox="0 0 14 20" aria-hidden="true">
          <rect x="1.5" y="1" width="11" height="18" rx="2" fill="none" stroke="var(--lime)" stroke-width="1.6"/>
          <line x1="5.5" y1="16" x2="8.5" y2="16" stroke="var(--lime)" stroke-width="1.4"/>
        </svg>
        <span>+505 8290 3357</span>
      </li>
      <li class="email">
        <svg width="16" height="12" viewBox="0 0 16 12" aria-hidden="true">
          <rect x="0" y="0" width="16" height="12" rx="1" fill="var(--lime)"/>
          <polyline points="1,1.5 8,7 15,1.5" fill="none" stroke="var(--paper)" stroke-width="1.2"/>
        </svg>
        <span>mkd@brevarconsulting-example.com</span>
      </li>
    </ul>

    <p class="company">Brevar Consulting a Tall Heron Investment Company SA.<br>RUC K0720000483915</p>
    <p class="website">www.brevarconsulting-example.com</p>
  </section>

</main>
</body>
</html>
```